Indie Poet needs book cover!

I am looking for a design that will sell my poetry book. My poems deal with themes of neurotic and dark Gothic narrative. A combination of these two styles is ideal.

The dimensions for the book cover are:

Place 5mm bleed around entire cover.

Width: 148mm (back) + 4.45mm (spine) + 148mm (front)

Height: 220mm

Front Cover:

Book Title: Under the Lantern, Under the Ashes: The Verse of Delia Marrowby

Author: Delia Marrowby

Please place the 'Editor's Choice' logo on the front cover. Beneath it, please put : quillscopeOCEANIA 2014 - For the poem 'Waiting by a Window'.

Spine: Under the Lantern, Under the Ashes: The Verse of Delia Marrowby

Back Cover:

Include 'The Widow' picture on the back cover.

Text:

About the book:
'Under the Lantern, Under the Ashes' is an impressive work for a debut release, featuring poems that have a maturity and level of experience you’d expect from poets who have been in the industry for decades. The poems and stories are complex, yet easy to associate with, and there would be few readers who wouldn't find themselves resonating with the themes. For all the cynicism and neuroticism, there is an underlying story about life and people.

Note: please leave SPACE for barcode. Do not add a barcode, just leave room for one.

```html
<!DOCTYPE html>
<html lang="en">
<head>
<meta charset="utf-8">
<title>Under the Lantern, Under the Ashes — Cover</title>
<link rel="stylesheet" href="https://fonts.googleapis.com/css2?family=Courier+Prime:ital,wght@0,400;0,700;1,400&display=swap">
<style>
  :root {
    --stage: #e4e5e5;
    --forest-light: #4f6250;
    --forest-mid: #2c3b30;
    --forest-deep: #121a16;
    --cover-edge: #0c100e;
    --linen: #d9d9d8;
    --linen-dark: #c9c9c8;
    --ink: #1d1d1d;
    --paper-white: #f4f4f2;
    --badge-gold: #c9a437;
    --widow-red: #b9524a;
    --widow-dark: #3b3434;
    --widow-skin: #cfc6c0;
  }
  * { box-sizing: border-box; margin: 0; padding: 0; }
  html, body {
    width: 1200px; height: 850px; overflow: hidden;
    background: var(--stage);
  }
  .book-wrap {
    position: absolute; left: 108px; top: 65px;
    width: 984px; height: 720px;
    display: flex;
    box-shadow: 0 12px 30px rgba(0,0,0,.18);
  }

  /* Back cover */
  .back-cover {
    width: 484px; height: 720px; position: relative;
    background: linear-gradient(160deg, var(--linen) 0%, var(--linen-dark) 100%);
    color: var(--ink);
    font-family: "Courier Prime", "Courier New", monospace;
  }
  .widow-art {
    position: absolute; left: 150px; top: 40px;
    width: 190px; height: 320px;
    border-radius: 46% 46% 30% 30% / 22% 22% 12% 12%;
    background: linear-gradient(180deg, var(--widow-dark) 0%, var(--widow-skin) 38%, var(--widow-red) 62%, var(--widow-red) 100%);
    opacity: .85;
  }
  .blurb {
    position: absolute; left: 44px; right: 44px; top: 372px;
    font-size: 14.5px; line-height: 1.28;
  }
  .blurb-heading {
    text-align: center; font-weight: 400; font-size: 14.5px;
    margin-bottom: 2px;
  }
  .blurb-body { text-align: justify; hyphens: auto; }
  .blurb-body strong { font-weight: 700; }

  /* Spine */
  .spine {
    width: 16px; height: 720px; position: relative;
    background: var(--linen-dark);
    border-left: 1px solid rgba(0,0,0,.08);
    border-right: 1px solid rgba(0,0,0,.15);
    overflow: hidden;
  }
  .spine-title {
    position: absolute; left: 50%; top: 50%;
    transform: translate(-50%, -50%) rotate(90deg);
    white-space: nowrap;
    font-family: "Courier Prime", "Courier New", monospace;
    font-weight: 700; font-size: 10px; color: var(--ink);
  }

  /* Front cover */
  .front-cover {
    width: 484px; height: 720px; position: relative; overflow: hidden;
    border: 3px solid var(--cover-edge);
    color: var(--paper-white);
    font-family: "Courier Prime", "Courier New", monospace;
  }
  .forest-scene {
    position: absolute; inset: 0;
    background:
      radial-gradient(ellipse at 45% 35%, rgba(120,140,120,.55) 0%, rgba(0,0,0,0) 55%),
      linear-gradient(180deg, var(--forest-light) 0%, var(--forest-mid) 45%, var(--forest-deep) 85%, #0a0f0c 100%);
  }
  .author-name {
    position: absolute; top: 128px; left: 0; right: 0;
    text-align: center; font-weight: 700; font-size: 47px;
    letter-spacing: 0.5px;
    text-shadow: 0 2px 4px rgba(0,0,0,.6);
  }
  .title-block {
    position: absolute; top: 296px; right: 20px; left: 20px;
    text-align: right;
  }
  .book-title {
    font-weight: 400; font-size: 23px; line-height: 1.1;
    text-shadow: 0 1px 3px rgba(0,0,0,.6);
  }
  .book-subtitle {
    font-style: italic; font-size: 21px; line-height: 1.1;
    padding-right: 22px;
    text-shadow: 0 1px 3px rgba(0,0,0,.6);
  }
  .award {
    position: absolute; left: 0; right: 0; bottom: 14px;
    text-align: center; font-weight: 700; font-size: 17px; line-height: 1.15;
  }
  .award-badge {
    width: 64px; height: 64px; border-radius: 50%;
    background: radial-gradient(circle at 35% 30%, #ecd27a 0%, var(--badge-gold) 60%, #9e7c22 100%);
    margin: 0 auto 8px;
  }
</style>
</head>
<body>
  <div class="book-wrap">
    <section class="back-cover">
      <div class="widow-art" role="img" aria-label="Watercolour illustration 'The Widow': a dark-haired woman in a red dress with a flower in her hair"></div>
      <div class="blurb">
        <p class="blurb-heading">About the book:</p>
        <p class="blurb-body"><strong>'Under the Lantern, Under the Ashes'</strong> is an impressive work for a debut release, featuring poems that have a maturity and level of experience you'd expect from poets who have been in the industry for decades. The poems and stories are complex, yet easy to associate with, and there would be few readers who wouldn't find themselves resonating with the themes. For all the cynicism and neuroticism, there is an underlying story about life and people.</p>
      </div>
    </section>

    <section class="spine">
      <p class="spine-title">Under the Lantern, Under the Ashes: The Verse of Delia Marrowby</p>
    </section>

    <section class="front-cover">
      <div class="forest-scene" role="img" aria-label="Misty dark green forest of bare tree trunks"></div>
      <h1 class="author-name">Delia Marrowby</h1>
      <div class="title-block">
        <h2 class="book-title">Under the Lantern, Under the Ashes</h2>
        <p class="book-subtitle">The Verse of Delia Marrowby</p>
      </div>
      <div class="award">
        <div class="award-badge" role="img" aria-label="Editor's Choice award seal"></div>
        <p>quillscopeOCEANIA 2014 -</p>
        <p>For the poem 'Waiting by a Window'.</p>
      </div>
    </section>
  </div>
</body>
</html>
```